依頼概要
■依頼目的 / 概要
電子書籍Lumora本を出版いたしますので、
表紙デザイン作成をお願いいたします。

■納品物
下記での納品をお願い致します。

JPEG形式 及び PSD形式
横1600ピクセル x 縦2560ピクセル

■本の内容

<本のタイトル>
ソラノワ-SKY RING-
老職人に学んだ
はじめての家庭づくりのガイドブック

<著者名>
浅井徹郎

■デザイン要望
・本のタイトル / 著者名の反映をお願いします

デザインイメージ

・基本的に青系の色合い

・シンプルな背景にタイトル等のコピーを記載

・ターゲットは子どもを持つご両親。

・お子様の子育てに関する細かいノウハウというよりも、
最も要となる考え方をお伝えしています。

・信頼感のあるデザインを希望します。

<表現したいイメージなど>
・信頼感

<表現したくないイメージ>
・安っぽい
・嘘くさい
・大衆的

<利用画像について>
画像素材を使用される場合には、
商用利用可の素材をお願いします。

■その他
デザインを考えるのに必要な情報が他にございましたら、
お答えしますので、遠慮なくご連絡ください。

*添付ファイルは、過去電子書籍の表紙デザインです。
*ジャンルが異なりますので、デザインテイストは今回とは、異なります。
*あくまでも、表紙に出てくる要素(タイトルや著者名など)の参考としてご利用ください。

意図をしっかりとご理解いただき、
目につく素晴らしいデザインに仕上げていただきました。
ありがとうございます。

この度は応募いただきありがとうございました。
近いうちにまた同じく、表紙のデザインをお願いする予定です。
またご参加くださいませ。

```html
<!DOCTYPE html>
<html lang="ja">
<head>
<meta charset="utf-8">
<title>ソラノワ -SKY RING- 表紙</title>
<link rel="stylesheet" href="https://fonts.googleapis.com/css2?family=Archivo+Black&family=Noto+Sans+JP:wght@500;700;900&display=swap">
<style>
  :root {
    --paper: #ffffff;
    --ink: #111111;
    --sky: #3ba4dc;
    --sky-deep: #2f93cf;
    --paper-cut: #eef6fb;
    --paper-shade: #c9e2f2;
    --brand-blue: #1f86d0;
    --accent-red: #d9262b;
  }
  * { margin: 0; padding: 0; box-sizing: border-box; }
  html, body { width: 750px; height: 1200px; overflow: hidden; background: var(--paper); }
  .cover {
    position: relative; width: 750px; height: 1200px; overflow: hidden;
    background: var(--paper);
    font-family: "Noto Sans JP", sans-serif;
  }
  .series-mark {
    position: absolute; top: -12px; left: 0; width: 750px; height: 70px;
    font-family: "Archivo Black", sans-serif; font-size: 74px; line-height: 70px;
    color: var(--ink); text-align: center; letter-spacing: 18px; padding-left: 18px;
    white-space: nowrap;
  }
  .hero {
    position: absolute; top: 55px; left: 0; width: 750px; height: 795px;
    background: linear-gradient(180deg, var(--sky) 0%, var(--sky-deep) 100%);
  }
  .hero-title {
    position: absolute; top: 100px; width: 100%; text-align: center;
    font-weight: 900; font-size: 70px; line-height: 1.1; color: var(--paper); letter-spacing: 4px;
  }
  .author { position: absolute; top: 228px; width: 100%; text-align: center; color: var(--ink); }
  .author-name { font-weight: 900; font-size: 36px; letter-spacing: 8px; display: block; line-height: 1.2; }
  .author-roman { font-weight: 700; font-size: 13px; letter-spacing: 2px; display: block; margin-top: 2px; }
  .family-art {
    position: absolute; top: 300px; left: 0; width: 750px; height: 440px;
    background:
      linear-gradient(180deg, rgba(238,246,251,0) 0%, rgba(238,246,251,0.85) 22%, var(--paper-cut) 55%, var(--paper-shade) 100%);
  }
  .divider { position: absolute; left: 225px; top: 750px; }
  .copy-badge {
    position: absolute; left: 50px; top: 900px; width: 175px; height: 175px;
    border: 5px solid var(--accent-red); border-radius: 50%; background: var(--paper);
    display: flex; flex-direction: column; align-items: center; justify-content: center;
    color: var(--accent-red); font-weight: 900; line-height: 1.05;
  }
  .copy-badge .big { font-size: 38px; }
  .copy-badge .small { font-size: 22px; }
  .growth-icon { position: absolute; left: 240px; top: 872px; }
  .subtitle-lead {
    position: absolute; left: 345px; top: 862px;
    font-weight: 900; font-size: 48px; color: var(--brand-blue); letter-spacing: 2px; line-height: 1.2;
  }
  .subtitle-main {
    position: absolute; right: 28px; top: 940px;
    font-weight: 900; font-size: 80px; color: var(--brand-blue); line-height: 1.1;
  }
  .subtitle-main .particle { font-size: 58px; }
  .subtitle-tail {
    position: absolute; right: 25px; top: 1060px;
    font-weight: 900; font-size: 82px; color: var(--brand-blue); line-height: 1.1; letter-spacing: 2px;
  }
</style>
</head>
<body>
  <main class="cover">
    <div class="series-mark">SKY RING</div>

    <section class="hero">
      <h1 class="hero-title">ソラノワ</h1>
      <p class="author">
        <span class="author-name">浅井 徹郎</span>
        <span class="author-roman">ASAI TETSURO</span>
      </p>
      <div class="family-art" role="img" aria-label="手で支えられた紙切りの家族（両親と二人の子どもが手をつなぐ）の写真"></div>
      <svg class="divider" width="300" height="24" viewBox="0 0 300 24" aria-hidden="true">
        <line x1="10" y1="6" x2="290" y2="6" stroke="#ffffff" stroke-width="2"/>
        <line x1="10" y1="18" x2="290" y2="18" stroke="#ffffff" stroke-width="2"/>
        <rect x="144" y="6" width="12" height="12" transform="rotate(45 150 12)" fill="#ffffff"/>
      </svg>
    </section>

    <div class="copy-badge">
      <span class="big">老職人</span>
      <span class="small">に</span>
      <span class="big">学んだ</span>
    </div>

    <svg class="growth-icon" width="100" height="46" viewBox="0 0 100 46" aria-hidden="true">
      <rect x="0" y="36" width="15" height="10" fill="#bfe0f4"/>
      <rect x="20" y="28" width="15" height="18" fill="#8ccbee"/>
      <rect x="40" y="20" width="15" height="26" fill="#5cb3e6"/>
      <rect x="60" y="11" width="15" height="35" fill="#3a9ddc"/>
      <rect x="80" y="2" width="15" height="44" fill="#1f86d0"/>
    </svg>

    <p class="subtitle-lead">はじめての</p>
    <p class="subtitle-main">家庭づくり<span class="particle">の</span></p>
    <p class="subtitle-tail">ガイドブック</p>
  </main>
</body>
</html>
```